Rooted Ready Rising: Quiet Roots, Open Doors, Steady Hands

I want a modern and clean looking book cover. 5.25x8

Title
Rooted Ready Rising

Subtitle
Quiet Roots, Open Doors, Steady Hands

I don’t just want a graphic, I want it to make sense. If it can just be the words and a textured looking background, I’ll be ok with that too. I just want it to look crisp, clean, modern.

I want the back to have my book blurb and bio attached with the pic that’s attached.

Target Market(s)

Self help

Requirements
Must have
• Modern, clean look, look professional, attract customers.

```html
<!DOCTYPE html>
<html lang="en">
<head>
<meta charset="utf-8">
<title>Rooted Ready Rising – Book Cover</title>
<link rel="stylesheet" href="https://fonts.googleapis.com/css2?family=Archivo+Black&family=Big+Shoulders+Display:wght@800;900&display=swap">
<style>
  :root {
    --ink: #0b0b0b;
    --band-top: #ffd60a;
    --band-bottom: #ffb000;
    --blush-edge: #f6b9c2;
    --blush-mid: #fde3e7;
    --blush-light: #fff6f7;
    --spine-shade: #d98f9b;
  }
  html, body {
    margin: 0;
    padding: 0;
    width: 769px;
    height: 1200px;
    overflow: hidden;
    background: #ffffff;
  }
  .cover {
    display: block;
    width: 769px;
    height: 1200px;
  }
  .title-line {
    font-family: "Big Shoulders Display", "Arial Narrow", sans-serif;
    font-weight: 900;
    fill: var(--ink);
  }
  .subtitle-line,
  .author-name {
    font-family: "Archivo Black", "Arial Black", sans-serif;
    fill: var(--ink);
  }
  .rule {
    stroke: var(--ink);
    stroke-width: 3;
  }
</style>
</head>
<body>
<svg class="cover" viewBox="0 0 769 1200" xmlns="http://www.w3.org/2000/svg" aria-label="Rooted Ready Rising book cover">
  <defs>
    <linearGradient id="blush-left" x1="0" x2="1" y1="0" y2="0">
      <stop offset="0" stop-color="var(--blush-edge)"/>
      <stop offset="0.55" stop-color="var(--blush-light)"/>
      <stop offset="1" stop-color="var(--blush-mid)"/>
    </linearGradient>
    <linearGradient id="blush-right" x1="0" x2="1" y1="0" y2="0">
      <stop offset="0" stop-color="var(--blush-light)"/>
      <stop offset="0.5" stop-color="var(--blush-mid)"/>
      <stop offset="1" stop-color="var(--blush-edge)"/>
    </linearGradient>
    <linearGradient id="band-fill" x1="0" x2="0" y1="0" y2="1">
      <stop offset="0" stop-color="var(--band-top)"/>
      <stop offset="1" stop-color="var(--band-bottom)"/>
    </linearGradient>
    <linearGradient id="band-shadow" x1="0" x2="1" y1="0" y2="0">
      <stop offset="0" stop-color="#000" stop-opacity="0.18"/>
      <stop offset="1" stop-color="#000" stop-opacity="0"/>
    </linearGradient>
    <linearGradient id="portrait-fill" x1="0" x2="0" y1="0" y2="1">
      <stop offset="0" stop-color="#3a2620"/>
      <stop offset="0.5" stop-color="#151515"/>
      <stop offset="0.62" stop-color="#e9e6e6"/>
      <stop offset="1" stop-color="#f7f4f4"/>
    </linearGradient>
  </defs>

  <!-- side panels -->
  <rect class="panel-left" x="0" y="0" width="180" height="1200" fill="url(#blush-left)"/>
  <rect class="spine-crease" x="20" y="0" width="10" height="1200" fill="var(--spine-shade)" opacity="0.35"/>
  <rect class="panel-right" x="592" y="0" width="177" height="1200" fill="url(#blush-right)"/>
  <rect class="band-cast" x="592" y="0" width="40" height="1200" fill="url(#band-shadow)"/>

  <!-- central band -->
  <rect class="title-band" x="180" y="0" width="412" height="1200" fill="url(#band-fill)"/>

  <!-- author portrait (beside the band, clear of the text) -->
  <rect class="author-portrait" x="596" y="500" width="173" height="700" rx="6"
        fill="url(#portrait-fill)" role="img"
        aria-label="Photo of the smiling author, hands on hips, wearing a black slogan T-shirt and white ripped jeans"/>

  <!-- title -->
  <text class="title-line" x="212" y="272" font-size="260" textLength="347" lengthAdjust="spacingAndGlyphs">ROOTED</text>
  <text class="title-line" x="212" y="472" font-size="231" textLength="347" lengthAdjust="spacingAndGlyphs">READY</text>
  <text class="title-line" x="212" y="762" font-size="334" textLength="347" lengthAdjust="spacingAndGlyphs">RISING</text>

  <!-- subtitle -->
  <line class="rule" x1="212" y1="852" x2="561" y2="852"/>
  <text class="subtitle-line" x="212" y="908" font-size="44" textLength="349" lengthAdjust="spacingAndGlyphs">QUIET ROOTS</text>
  <text class="subtitle-line" x="212" y="958" font-size="44" textLength="349" lengthAdjust="spacingAndGlyphs">OPEN DOORS</text>
  <text class="subtitle-line" x="214" y="1003" font-size="33" textLength="347" lengthAdjust="spacingAndGlyphs">STEADY HANDS</text>
  <line class="rule" x1="212" y1="1025" x2="561" y2="1025"/>

  <!-- author -->
  <text class="author-name" x="208" y="1163" font-size="46" textLength="351" lengthAdjust="spacingAndGlyphs">AUTHOR NAME</text>
</svg>
</body>
</html>
```